Dravell PowerPoint Theme/Template

I want to be able to put together presentations that have a cohesive look and work with my current branding on my website (www.dravell.com) and social media (#dravellskincare).

```html
<!DOCTYPE html>
<html lang="en">
<head>
<meta charset="utf-8">
<title>Dravell – Three Point Slide</title>
<link rel="stylesheet" href="https://fonts.googleapis.com/css2?family=Carlito:wght@400;700&display=swap">
<style>
  :root {
    --brand-brown: #9a5b2a;
    --line-brown: #96602f;
    --sand: #e6c3a3;
    --sand-rule: #ecd3ba;
    --paper: #ffffff;
  }
  * { margin: 0; padding: 0; box-sizing: border-box; }
  html, body { width: 1200px; height: 674px; overflow: hidden; background: var(--paper); }
  body { font-family: "Carlito", "Calibri", sans-serif; color: var(--brand-brown); }

  .slide { position: relative; width: 1200px; height: 674px; overflow: hidden; }

  .brand-tag {
    position: absolute; left: 11px; top: 9px;
    font-size: 13px; font-weight: 400; white-space: nowrap;
  }
  .top-bar {
    position: absolute; left: 189px; top: 15px; width: 460px; height: 4px;
    background: var(--line-brown);
  }
  .slide-title {
    position: absolute; left: 0; top: 61px; width: 1200px; text-align: center;
    font-size: 38px; font-weight: 700; letter-spacing: 0.2px; line-height: 1;
  }
  .title-rule {
    position: absolute; left: 37px; top: 102px; width: 1134px; height: 1px;
    background: var(--sand-rule);
  }

  .point-card { position: absolute; top: 200px; width: 300px; height: 340px; }
  .point-card svg { position: absolute; left: 0; top: 0; }
  .point-number {
    position: absolute; left: 49px; top: 62px; width: 60px; text-align: center;
    font-size: 27px; font-weight: 700; line-height: 32px;
  }
  .point-heading {
    position: absolute; left: 102px; top: 54px; width: 80px; text-align: center;
    font-size: 16.5px; font-weight: 700; line-height: 20.5px;
  }
  .point-body {
    position: absolute; left: 56px; top: 138px; width: 188px; text-align: center;
    font-size: 13.6px; line-height: 18.1px;
  }

  .bottom-bar {
    position: absolute; left: 601px; top: 656px; width: 460px; height: 4px;
    background: var(--line-brown);
  }
  .tagline {
    position: absolute; left: 1079px; top: 649px;
    font-size: 13px; white-space: nowrap;
  }
</style>
</head>
<body>
<main class="slide">
  <div class="brand-tag">Dravell by dr. Elise Marrow</div>
  <div class="top-bar"></div>

  <h1 class="slide-title">TITLE GOES HERE</h1>
  <div class="title-rule"></div>

  <section class="point-card" style="left:144px">
    <svg width="300" height="340" viewBox="0 0 300 340" aria-hidden="true">
      <circle cx="150" cy="202" r="132" fill="none" stroke="var(--sand)" stroke-width="3"/>
      <circle cx="144" cy="73" r="62" fill="var(--paper)" stroke="var(--sand)" stroke-width="2.5"/>
      <circle cx="79" cy="78" r="30.5" fill="var(--sand)"/>
    </svg>
    <div class="point-number">01</div>
    <h2 class="point-heading">Title<br>One</h2>
    <p class="point-body">Lorem Ipsum is simply dummy text of the printing and typesetting industry. Lorem Ipsum has been the industry's standard dummy text ever since the 1500s, when an unknown printer took a galley of type and scrambled it to make a type specimen book</p>
  </section>

  <section class="point-card" style="left:470px">
    <svg width="300" height="340" viewBox="0 0 300 340" aria-hidden="true">
      <circle cx="150" cy="202" r="132" fill="none" stroke="var(--sand)" stroke-width="3"/>
      <circle cx="144" cy="73" r="62" fill="var(--paper)" stroke="var(--sand)" stroke-width="2.5"/>
      <circle cx="79" cy="78" r="30.5" fill="var(--sand)"/>
    </svg>
    <div class="point-number">02</div>
    <h2 class="point-heading">Title<br>Two</h2>
    <p class="point-body">Lorem Ipsum is simply dummy text of the printing and typesetting industry. Lorem Ipsum has been the industry's standard dummy text ever since the 1500s, when an unknown printer took a galley of type and scrambled it to make a type specimen book</p>
  </section>

  <section class="point-card" style="left:797px">
    <svg width="300" height="340" viewBox="0 0 300 340" aria-hidden="true">
      <circle cx="150" cy="202" r="132" fill="none" stroke="var(--sand)" stroke-width="3"/>
      <circle cx="144" cy="73" r="62" fill="var(--paper)" stroke="var(--sand)" stroke-width="2.5"/>
      <circle cx="79" cy="78" r="30.5" fill="var(--sand)"/>
    </svg>
    <div class="point-number">03</div>
    <h2 class="point-heading">Title<br>Three</h2>
    <p class="point-body">Lorem Ipsum is simply dummy text of the printing and typesetting industry. Lorem Ipsum has been the industry's standard dummy text ever since the 1500s, when an unknown printer took a galley of type and scrambled it to make a type specimen book</p>
  </section>

  <div class="bottom-bar"></div>
  <div class="tagline">Love for your skin</div>
</main>
</body>
</html>
```